Zertifikat-Design für Bildungsträger im Bereich der Erwachsenenbildung
Zielgruppe
Talwerk Akademie - Zertifizierter Bildungsträger im Bereich der Erwachsenenbildung. Überwiegend Mitarbeiter in Unternehmen.
Aufgabenstellung
'Erstelle ein hochwertiges, modernes und exklusiv wirkendes Zertifikat für die Talwerk Akademie. Das Design soll professionell, minimalistisch und zugleich edel sein. Ziel ist es, ein Dokument zu gestalten, das den Eindruck vermittelt: 'Das ist das einzige und beste Zertifikat in der ganzen verdammten Welt.'
Das Zertifikat soll im Querformat (idealerweise DIN A4 horizontal) gestaltet werden. Der Inhalt soll zweisprachig (Deutsch und Englisch) dargestellt werden, klar gegliedert und typografisch hochwertig aufgebaut. Alle Inhalte sollten mittig ausgerichtet sein, mit gut erkennbarer visueller Hierarchie.
Der Haupttext lautet wie folgt:
'Talwerk Akademie gratuliert 'Name / Platzhalter' zum erfolgreichen Abschluss des Kurses 'Platzhalter' Datum, Unterschrift (siehe unten)
+englisch
'Talwerk Akademie hereby certifies that [Name of Participant / Placeholder] has successfully participated on 'date'.
Darunter sollen zwei stilisierte Unterschriften platziert werden – gerne von Hand gezeichnet oder elegant typografisch umgesetzt. Die Beschriftung unter den Unterschriften lautet: 'Leitung Talwerk Akademie'.
Ein zentrales Element ist das Hologramm. Muster das gelieferte Bild 'Hologramm.png'. Es muss deutlich sichtbar und hochwertig integriert werden. Die Aufschrift 'Talwerk' im Hologramm muss klar erkennbar sein. Idealer Platz wäre unten links oder rechts, eventuell mit einer leichten 3D-Anmutung oder Glanzeffekt.
Das gesamte Design muss der Corporate Identity der Talwerk Akademie entsprechen. Die verwendeten Farben sind: Hauptfarbe Dunkelblau (RGB 14, 32, 62), ergänzt durch Hellblau (RGB 241, 245, 250), ein zusätzliches Blau (RGB 65, 111, 174), Pink (RGB 140, 130, 227), Dunkellila (RGB 169, 97, 161), sowie Gelb (RGB 248, 216, 73) und Orange (RGB 220, 121, 70) für gezielte Akzente.
Als Schriftart ist ausschließlich Roboto zu verwenden. Der Name des Teilnehmers soll besonders hervorgehoben werden (z...

```html
<!DOCTYPE html>
<html lang="de">
<head>
<meta charset="utf-8">
<title>Zertifikat – Talwerk Akademie</title>
<link href="https://fonts.googleapis.com/css2?family=Roboto:wght@400;500;700&display=swap" rel="stylesheet">
<style>
  :root {
    --navy: #0e1f3e;
    --navy-deep: #011a3d;
    --light-blue: #f1f5fa;
    --paper: #ffffff;
    --backdrop: #d9dbda;
    --gold-dark: #b8831f;
    --gold-light: #f3da7a;
  }
  html, body {
    margin: 0;
    padding: 0;
    width: 1200px;
    height: 1199px;
    overflow: hidden;
    background: var(--backdrop);
    font-family: "Roboto", sans-serif;
    color: var(--navy);
  }
  .certificate {
    position: absolute;
    left: 69px;
    top: 224px;
    width: 1063px;
    height: 708px;
    background: var(--paper);
    overflow: hidden;
  }
  .certificate__frame {
    position: absolute;
    inset: 0;
    width: 100%;
    height: 100%;
  }
  .certificate__text {
    position: absolute;
    left: 0;
    width: 100%;
    margin: 0;
    text-align: center;
    text-transform: uppercase;
  }
  .title {
    top: 111px;
    font-size: 31px;
    font-weight: 700;
    line-height: 39px;
    letter-spacing: 0.2px;
  }
  .title-en {
    top: 204px;
    font-size: 13px;
    font-weight: 700;
    letter-spacing: 0.2px;
  }
  .participant {
    top: 272px;
    font-size: 45px;
    font-weight: 500;
    letter-spacing: 0.6px;
  }
  .participant-rule {
    position: absolute;
    left: 330px;
    top: 328px;
    width: 403px;
    height: 3px;
    background: linear-gradient(90deg, var(--gold-dark), var(--gold-light), var(--gold-dark));
  }
  .completion {
    top: 373px;
    font-size: 17.5px;
    font-weight: 400;
  }
  .completion-en {
    top: 397px;
    font-size: 12.5px;
    font-weight: 400;
    letter-spacing: 0.3px;
  }
  .course {
    top: 435px;
    font-size: 22px;
    font-weight: 400;
    letter-spacing: 0.4px;
  }
  .signature {
    position: absolute;
    width: 150px;
    text-align: center;
  }
  .signature--left { left: 330px; top: 496px; }
  .signature--right { left: 586px; top: 493px; }
  .signature__mark {
    display: block;
    width: 150px;
    height: 74px;
    background: linear-gradient(120deg, rgba(14,31,62,0.05), rgba(14,31,62,0.14), rgba(14,31,62,0.05));
    border-radius: 4px;
  }
  .signature__rule {
    height: 2px;
    background: linear-gradient(90deg, var(--gold-dark), var(--gold-light), var(--gold-dark));
  }
  .signature__label {
    margin-top: 4px;
    font-size: 8.5px;
    letter-spacing: 0.5px;
    text-transform: uppercase;
    white-space: nowrap;
  }
  .seal {
    position: absolute;
    left: 112px;
    top: 446px;
    width: 140px;
    height: 140px;
  }
  .hologram {
    position: absolute;
    left: 785px;
    top: 434px;
    width: 144px;
    height: 144px;
    border-radius: 50%;
    background:
      radial-gradient(circle at 35% 30%, rgba(255,255,255,0.85), rgba(255,255,255,0) 45%),
      conic-gradient(from 40deg, #e9d6f0, #cfe9f6, #f6f1c8, #d8f0d6, #e6d3f3, #cde2f7, #e9d6f0);
    box-shadow: 3px 4px 8px rgba(0,0,0,0.18);
  }
</style>
</head>
<body>
  <main class="certificate">
    <svg class="certificate__frame" viewBox="0 0 1108 738" preserveAspectRatio="none" aria-hidden="true">
      <defs>
        <linearGradient id="gold" x1="0" y1="0" x2="1" y2="0">
          <stop offset="0" stop-color="#b8831f"/>
          <stop offset="0.55" stop-color="#f3da7a"/>
          <stop offset="1" stop-color="#b8831f"/>
        </linearGradient>
      </defs>
      <rect x="33" y="30" width="1043" height="679" fill="none" stroke="url(#gold)" stroke-width="3.5"/>
      <polygon points="0,0 446,0 0,182" fill="#011a3d"/>
      <polygon points="140,27 418,27 385,74 160,74 0,255 0,182" fill="#f1f5fa"/>
      <polygon points="660,738 1108,738 1108,555" fill="#011a3d"/>
      <polygon points="1108,484 1108,555 968,711 688,711 718,663 950,663" fill="#f1f5fa"/>
    </svg>

    <h1 class="certificate__text title">Talwerk Akademie<br>gratuliert</h1>
    <p class="certificate__text title-en">Talwerk Akademie hereby certifies that</p>
    <p class="certificate__text participant">Max Mustermann</p>
    <div class="participant-rule"></div>
    <p class="certificate__text completion">Zum erfolgreichen Abschluss des Kurses:</p>
    <p class="certificate__text completion-en">Has successfully participated on:</p>
    <p class="certificate__text course">Kurs Platzhalter, Datum</p>

    <svg class="seal" viewBox="0 0 140 140" role="img" aria-label="Goldenes Zertifikatssiegel">
      <defs>
        <radialGradient id="seal-gold" cx="0.4" cy="0.35" r="0.7">
          <stop offset="0" stop-color="#f6e08a"/>
          <stop offset="0.6" stop-color="#d9a93a"/>
          <stop offset="1" stop-color="#a8741c"/>
        </radialGradient>
      </defs>
      <circle cx="70" cy="70" r="68" fill="url(#seal-gold)"/>
      <circle cx="70" cy="70" r="50" fill="#0e1f3e" stroke="#e8c565" stroke-width="3"/>
    </svg>

    <div class="signature signature--left">
      <span class="signature__mark" role="img" aria-label="Handschriftliche Unterschrift der Akademieleitung"></span>
      <div class="signature__rule"></div>
      <div class="signature__label">Leitung Talwerk Akademie</div>
    </div>
    <div class="signature signature--right">
      <span class="signature__mark" role="img" aria-label="Handschriftliche Unterschrift der Akademieleitung"></span>
      <div class="signature__rule"></div>
      <div class="signature__label">Leitung Talwerk Akademie</div>
    </div>

    <div class="hologram" role="img" aria-label="Schillerndes Hologramm-Siegel mit Talwerk-Schriftzug"></div>
  </main>
</body>
</html>
```